Modern Business Card Design for Independent Urban Music Label

We need a card design for an independent urban music label called Copper Kite Records based in London. We develop and promote urban British music artists. We attend lots of high profile events with high profile industry people and want a card that comes across both on-brand and sophisticated, professional, trustworthy. I have attached our logo - please use the black and orange version in the upper left HOWEVER we are open to seeing other colors than the orange used though we want the shape of the logo to remain the same.

Info to please include:
Name
Position
Phone
Email
Website

Additional Info:
Twitter: @CopperKiteRecsUK
Insta: @CopperKiteRecs

Target Market(s)

Industry professionals and others artists

Industry/Entity Type

Business

Contact Information for Business Card

Info to please include:
Name
Position
Phone
Email
Website

Additional Info:
Twitter: @CopperKiteRecsUK
Insta: @CopperKiteRecs

Requirements
Must have
• Logo, company name
• Info to please include:
• Name
• Position
• Phone
• Email
• Website
Nice to have
• Twitter: @CopperKiteRecsUK
• Insta: @CopperKiteRecs
• If it can be done so that it doesn't look cluttered

```html
<!DOCTYPE html>
<html lang="en">
<head>
<meta charset="utf-8">
<title>Copper Kite Records – Business Card</title>
<link rel="stylesheet" href="https://fonts.googleapis.com/css2?family=Open+Sans:wght@400;600;700&display=swap">
<style>
  :root {
    --backdrop: #ebeceb;
    --card: #ffffff;
    --copper: #f4914f;
    --copper-faint: rgba(255, 255, 255, 0.38);
    --ink: #2d2a29;
    --text: #2e2e2e;
  }
  * { margin: 0; padding: 0; box-sizing: border-box; }
  html, body {
    width: 1022px;
    height: 1200px;
    overflow: hidden;
    background: var(--backdrop);
    font-family: "Open Sans", Arial, sans-serif;
    color: var(--text);
  }
  .card {
    position: absolute;
    width: 761px;
    height: 479px;
    background: var(--card);
    overflow: hidden;
    box-shadow: 0 2px 6px rgba(0, 0, 0, 0.18);
  }
  .card--front { left: 105px; top: 75px; }
  .card--back { left: 113px; top: 614px; }
  .card__band {
    position: absolute;
    inset: 0;
    width: 100%;
    height: 100%;
  }
  .card__band polygon { fill: var(--copper); }

  .brand-mark {
    position: absolute;
    border-radius: 50%;
  }
  .card--front .brand-mark {
    left: 184px; top: 121px;
    width: 130px; height: 130px;
    background: var(--ink);
  }
  .card--back .brand-mark {
    left: 493px; top: 175px;
    width: 150px; height: 150px;
    background: var(--copper-faint);
  }
  .brand-name {
    position: absolute;
    width: 420px;
    text-align: center;
    font-weight: 600;
    font-size: 30px;
    letter-spacing: 2px;
    text-transform: uppercase;
    white-space: nowrap;
  }
  .card--front .brand-name { left: 41px; top: 378px; color: #ffffff; }
  .card--back .brand-name { left: 358px; top: 405px; color: var(--copper-faint); }

  .contact-list { position: absolute; list-style: none; }
  .contact-list li {
    display: flex;
    align-items: center;
    height: 43px;
    font-size: 23px;
    white-space: nowrap;
  }
  .contact-list .icon {
    width: 24px;
    height: 24px;
    margin-right: 14px;
    flex: none;
  }
  .icon--square {
    border-radius: 3px;
    background: var(--copper);
    width: 22px !important;
    height: 22px !important;
  }
  .card--front .contact-list { left: 347px; top: 108px; }
  .card--back .contact-list { left: 52px; top: 140px; }
  .card--back .contact-list .icon { width: 22px; height: 22px; margin-right: 17px; }

  .holder { position: absolute; left: 59px; top: 62px; }
  .holder__name { font-size: 25px; font-weight: 700; line-height: 1.3; }
  .holder__role { font-size: 21px; line-height: 1.3; margin-top: 2px; }
</style>
</head>
<body>

<section class="card card--front" aria-label="Card front">
  <svg class="card__band" viewBox="0 0 761 479" preserveAspectRatio="none" aria-hidden="true">
    <polygon points="0,64 685,479 0,479"/>
  </svg>
  <div class="brand-mark" aria-hidden="true"></div>
  <p class="brand-name">Copper Kite Records</p>
  <ul class="contact-list">
    <li>
      <svg class="icon" viewBox="0 0 24 24" aria-hidden="true" fill="none" stroke="#f4914f" stroke-width="1.6">
        <circle cx="12" cy="12" r="10"/><ellipse cx="12" cy="12" rx="4.5" ry="10"/>
        <line x1="2" y1="12" x2="22" y2="12"/><line x1="12" y1="2" x2="12" y2="22"/>
      </svg>
      www.CopperKiteRecords.co.uk
    </li>
    <li><span class="icon icon--square" aria-hidden="true"></span>@CopperKiteRecsUK</li>
    <li><span class="icon icon--square" aria-hidden="true"></span>@CopperKiteRecs</li>
  </ul>
</section>

<section class="card card--back" aria-label="Card back">
  <svg class="card__band" viewBox="0 0 761 479" preserveAspectRatio="none" aria-hidden="true">
    <polygon points="76,479 761,65 761,479"/>
  </svg>
  <div class="brand-mark" aria-hidden="true"></div>
  <p class="brand-name">Copper Kite Records</p>

  <div class="holder">
    <p class="holder__name">Your Name</p>
    <p class="holder__role">Position</p>
  </div>
  <ul class="contact-list">
    <li>
      <svg class="icon" viewBox="0 0 24 24" aria-hidden="true">
        <path fill="#f4914f" d="M6.6 2.5l3 3.6-1.8 2.2c.9 2.6 3.3 5.4 6.1 6.9l2.1-1.7 3.5 3.1-1.6 3.2c-6.6.1-13.4-7.9-13.3-15.4z"/>
      </svg>
      123-456-7890
    </li>
    <li>
      <svg class="icon" viewBox="0 0 24 24" aria-hidden="true" fill="none" stroke="#f4914f" stroke-width="1.6">
        <rect x="2" y="5" width="20" height="14"/><polyline points="2,5 12,13 22,5"/>
      </svg>
      name@copperkiterecords.co.uk
    </li>
    <li>
      <svg class="icon" viewBox="0 0 24 24" aria-hidden="true" fill="none" stroke="#f4914f" stroke-width="1.6">
        <circle cx="12" cy="12" r="10"/><ellipse cx="12" cy="12" rx="4.5" ry="10"/>
        <line x1="2" y1="12" x2="22" y2="12"/><line x1="12" y1="2" x2="12" y2="22"/>
      </svg>
      www.copperkiterecords.co.uk
    </li>
  </ul>
</section>

</body>
</html>
```